Brim Vantage Partners Consulting Company Template

Microsoft Word template for a professional retail consulting company that can suggestingly mimic the attached design, but in vertical fashion - . Important - It doesn't have to mimic this design. I accept creativity, professionalism, and eye catching work!

I'd also like suggestingly the globe of the attached logo to appear as an imprint in the background

To win the contest, please make it look extremely impressive, attention grabbing, and don't fear giving it your own creative unique design elements.

The Word template is needed for me to create Word documents from, so it is highly important that I would be able to write memos in Word, and for those same memos to look clean.

Target Market(s)

Retailers interested in consulting services from Tolven Supply

Font styles to use
Serif

Requirements
Must have
• Brim Vantage Partners logo represented. Also, red and black logo colors. A professional, modern, outstanding look and design. Must be somewhat bold and upmarket.
Nice to have
• I accept all forms of creativity.
Should not have
• Cartoon / child looking

```html
<!DOCTYPE html>
<html lang="en">
<head>
<meta charset="utf-8">
<title>Brim Vantage Partners – Document Template</title>
<link href="https://fonts.googleapis.com/css2?family=Fira+Sans:wght@400;500;700&family=Great+Vibes&family=Tinos&display=swap" rel="stylesheet">
<style>
  :root{
    --bg:#d7dfe1;
    --red:#e8142a;
    --deep-red:#6b0a12;
    --ink:#1b1b1b;
    --muted:#6a7275;
    --paper:#ffffff;
    --night-top:#2b2b2b;
    --night-bottom:#111111;
    --rule:#9a9a9a;
  }
  *{margin:0;padding:0;box-sizing:border-box}
  html,body{width:1200px;height:1200px;overflow:hidden}
  body{background:var(--bg);font-family:"Fira Sans",Arial,sans-serif;position:relative}
  .page{position:absolute;background:var(--paper);overflow:hidden;box-shadow:6px 8px 10px rgba(0,0,0,.35)}

  /* Cover page */
  .cover{left:60px;top:155px;width:628px;height:878px}
  .brand{position:absolute;left:65px;top:72px}
  .brand-name{font-weight:700;font-size:32px;color:var(--ink);line-height:1;letter-spacing:.5px}
  .brand-line{font-weight:400;font-size:14px;color:var(--muted);margin-top:9px;letter-spacing:.2px}
  .cover-title{position:absolute;left:65px;top:184px;font-weight:700;font-size:58px;color:var(--red);letter-spacing:1.6px;line-height:1}
  .cover-subtitle{position:absolute;left:66px;top:244px;font-weight:700;font-size:29px;color:var(--ink);letter-spacing:.9px}
  .cover-band{position:absolute;left:0;top:300px}
  .cover-body{position:absolute;left:51px;top:453px;width:527px;color:#fff;font-size:13.8px;line-height:19.3px}
  .cover-body p:first-child{text-align:justify}
  .cover-body h2{font-family:"Great Vibes",cursive;font-weight:400;font-size:28px;margin:18px 0 12px -3px}

  /* Contents page */
  .contents{left:728px;top:35px;width:400px;height:558px}
  .contents h1{position:absolute;left:31px;top:40px;font-family:"Tinos",serif;font-weight:400;font-size:16.5px;color:var(--red);letter-spacing:.3px}
  .toc{position:absolute;left:33px;top:80px;width:340px;list-style:none;font-family:"Tinos",serif;font-size:9.5px;color:#333}
  .toc li{display:flex;align-items:baseline;height:19px}
  .toc li.gap{margin-top:4px}
  .toc .leader{flex:1;border-bottom:1px dotted var(--rule);margin:0 3px 0 2px;max-width:245px}
  .toc .num{margin-left:auto}
  .contents-band{position:absolute;left:0;top:430px}
  .page-badge{position:absolute;left:27px;top:465px;width:56px;height:56px;border-radius:50%;background:var(--red);border:3px solid #fff;color:#fff;font-size:28px;font-weight:500;display:flex;align-items:center;justify-content:center}
  .contents-url{position:absolute;right:24px;top:522px;color:#fff;font-size:12px}

  /* Back page */
  .back{left:728px;top:617px;width:397px;height:553px;background:linear-gradient(160deg,var(--night-top),var(--night-bottom))}
  .back-photo{position:absolute;inset:0;background:radial-gradient(ellipse at 55% 45%,rgba(90,90,90,.35),rgba(0,0,0,0) 70%)}
  .back-brand{position:absolute;left:0;right:0;top:258px;text-align:center;color:#fff}
  .back-brand .brand-name{color:#fff;font-size:28px}
  .back-brand .brand-line{color:#cfcfcf;font-size:13px}
  .back-address{position:absolute;left:0;right:0;top:503px;text-align:center;color:#ddd;font-size:10px}
  .back-contact{position:absolute;left:0;right:0;top:524px;text-align:center;color:#ddd;font-size:9.5px}
</style>
</head>
<body>

<section class="page cover">
  <div class="brand">
    <div class="brand-name">BRIM VANTAGE PARTNERS</div>
    <div class="brand-line">Retail Strategy &amp; Growth Advisory</div>
  </div>
  <h1 class="cover-title">YOUR TITLE HERE</h1>
  <p class="cover-subtitle">YOUR SUBTITLE HERE</p>

  <svg class="cover-band" width="628" height="578" viewBox="0 0 628 578">
    <defs>
      <linearGradient id="slate" x1="0" y1="0" x2="0" y2="1">
        <stop offset="0" stop-color="#5f6a6d"/>
        <stop offset="1" stop-color="#3c4244"/>
      </linearGradient>
    </defs>
    <polygon points="0,130 628,80 628,578 0,578" fill="url(#slate)"/>
    <polygon points="0,112 628,62 628,80 0,130" fill="#6b0a12"/>
    <polygon points="0,84 628,34 628,56 0,106" fill="#e8142a"/>
  </svg>

  <div class="cover-body">
    <p>Lorem Ipsum is simply dummy text of the printing and typesetting industry. Lorem Ipsum has been the industry's standard dummy text ever since the 1500s, when an unknown printer took a galley of type and scrambled it to make a type specimen book. It has survived not only five centuries, but also the leap into electronic typesetting, remaining essentially unchanged. It was popularised in the 1960s with the release of Letraset sheets containing Lorem Ipsum passages, and more recently with desktop publishing software like Aldus PageMaker including versions of Lorem Ipsum.</p>
    <h2>Why do we use it?</h2>
    <p>It is a long established fact that a reader will be distracted by the readable content of a page when looking at its layout. The point of using Lorem Ipsum is that it has a more-or-less normal distribution of letters, as opposed to using 'Content here, content here', making it look like readable English. Many desktop publishing packages and web page editors now use Lorem Ipsum as their default model text, and a search for 'lorem ipsum' will uncover many web sites still in their infancy. Various versions have evolved over the years, sometimes by accident, sometimes on purpose (injected humour and the like)</p>
  </div>
</section>

<section class="page contents">
  <h1>TABLE OF CONTENTS</h1>
  <ul class="toc">
    <li>Lorem Ipsum<span class="leader"></span><span class="num">1</span></li>
    <li>Lorem Ipsum<span class="leader"></span><span class="num">3</span></li>
    <li>Lorem Ipsum<span class="leader"></span><span class="num">3</span></li>
    <li>Lorem Ipsum<span class="leader"></span><span class="num">3</span></li>
    <li>Lorem Ipsum<span class="leader"></span><span class="num">4</span></li>
    <li>Lorem Ipsum<span class="leader"></span><span class="num">4</span></li>
    <li>Lorem Ipsum<span class="leader"></span><span class="num">4</span></li>
    <li class="gap">Lorem Ipsum<span class="leader"></span><span class="num">5</span></li>
    <li>Lorem Ipsum<span class="leader"></span><span class="num">5</span></li>
    <li>Lorem Ipsum<span class="leader"></span><span class="num">6</span></li>
    <li>Lorem Ipsum<span class="leader"></span><span class="num">6</span></li>
    <li>Lorem Ipsum<span class="leader"></span><span class="num">6</span></li>
    <li>Lorem Ipsum<span class="leader"></span><span class="num">7</span></li>
    <li>Lorem Ipsum<span class="leader"></span><span class="num">7</span></li>
  </ul>
  <svg class="contents-band" width="400" height="128" viewBox="0 0 400 128">
    <defs>
      <linearGradient id="slate2" x1="0" y1="0" x2="0" y2="1">
        <stop offset="0" stop-color="#5f6a6d"/>
        <stop offset="1" stop-color="#3c4244"/>
      </linearGradient>
    </defs>
    <polygon points="0,92 400,62 400,128 0,128" fill="url(#slate2)"/>
    <polygon points="0,80 400,50 400,62 0,92" fill="#6b0a12"/>
    <polygon points="0,62 400,32 400,46 0,76" fill="#e8142a"/>
  </svg>
  <div class="page-badge">2</div>
  <div class="contents-url">www.brimvantagepartners.com</div>
</section>

<section class="page back">
  <div class="back-photo" role="img" aria-label="Dimmed photograph of a desk with a laptop, notebook and pen"></div>
  <div class="back-brand">
    <div class="brand-name">BRIM VANTAGE PARTNERS</div>
    <div class="brand-line">Retail Strategy &amp; Growth Advisory</div>
  </div>
  <div class="back-address">Dummy City, Dummy Country, Land</div>
  <div class="back-contact">1-555-014-2090 | www.brimvantagepartners.com | nora@brimvantagepartners.com</div>
</section>

</body>
</html>
```